Bill board design For Marlowe’s Construction

Billboard Design Request
Please design the billboard to match the branding, colors, and overall feel of our website: Marlowe's Construction Website
MARLOWE’S CONSTRUCTION
CONCRETE BUILT FOR GENERATIONS
⭐ 5-Star Rated on Zorvix
Please Include:
* All three attached project photos
* Company logo(s)
* Phone Number: 555-214-7630
* Website: MarlowesConstruction.example
* Zorvix logo with 5-star rating graphic
* Chatterly logo
* Pixtoria logo
Service Area:
Kalamazoo • Battle Creek • Coldwater • Grand Rapids
Please arrange the photos and layout in whatever way creates the strongest visual impact and readability from the road. The company name, headline, phone number, and website should be highly visible at highway speeds.
The overall appearance should be clean, professional, premium, and consistent with our website branding while highlighting our reputation, craftsmanship, and quality concrete work.
People Driving By
Concrete Construction

```html
<!DOCTYPE html>
<html lang="en">
<head>
<meta charset="utf-8">
<title>Marlowe’s Construction — Billboard</title>
<link rel="stylesheet" href="https://fonts.googleapis.com/css2?family=Montserrat:ital,wght@0,400;0,600;0,700;0,800;0,900;1,800;1,900&display=swap">
<style>
  :root {
    --stage: #a4a4a4;
    --white: #ffffff;
    --ink: #050505;
    --brand-blue: #1592e6;
    --deep-blue: #0f5fc4;
    --slate: #5d6670;
    --star: #f5a623;
    --divider: #8a8a8a;
  }
  html, body {
    margin: 0;
    padding: 0;
    width: 1200px;
    height: 1200px;
    overflow: hidden;
    background: var(--stage);
    font-family: "Montserrat", Arial, sans-serif;
  }
  .billboard {
    position: absolute;
    left: 30px;
    top: 374px;
    width: 1140px;
    height: 452px;
    display: block;
  }
  .bg-white { fill: var(--white); }
  .bg-ink { fill: var(--ink); }
  .accent-blue { fill: var(--brand-blue); }
  .accent-deep { fill: var(--deep-blue); }
  .brand-name { font-weight: 800; fill: var(--brand-blue); font-size: 58px; }
  .brand-sub { font-weight: 400; fill: var(--slate); font-size: 27px; letter-spacing: 7px; }
  .headline-main { font-weight: 900; fill: var(--white); font-size: 122px; }
  .headline-mid { font-weight: 800; font-style: italic; fill: var(--brand-blue); font-size: 62px; }
  .headline-end { font-weight: 900; font-style: italic; fill: var(--white); font-size: 86px; }
  .rule { stroke: var(--deep-blue); stroke-width: 3; }
  .phone-number { font-weight: 800; fill: var(--ink); font-size: 70px; }
  .web-address { font-weight: 600; fill: var(--white); font-size: 34px; }
  .review-name { font-weight: 700; fill: var(--brand-blue); font-size: 66px; }
  .star { fill: var(--star); }
  .social-name { font-weight: 700; fill: var(--ink); font-size: 17px; }
  .city { font-weight: 800; font-size: 42px; letter-spacing: 3px; }
  .city-white { fill: var(--white); }
  .city-blue { fill: var(--brand-blue); }
</style>
</head>
<body>
<svg class="billboard" viewBox="0 0 1768 702" xmlns="http://www.w3.org/2000/svg" aria-label="Marlowe’s Construction billboard">
  <defs>
    <linearGradient id="crewTone" x1="0" y1="0" x2="1" y2="1">
      <stop offset="0" stop-color="#7b6a4c"/>
      <stop offset="0.5" stop-color="#4a3a2c"/>
      <stop offset="1" stop-color="#2c2a2e"/>
    </linearGradient>
    <linearGradient id="garageTone" x1="0" y1="0" x2="0" y2="1">
      <stop offset="0" stop-color="#6f7a5a"/>
      <stop offset="0.55" stop-color="#8a7466"/>
      <stop offset="1" stop-color="#d9d6cf"/>
    </linearGradient>
    <linearGradient id="walkTone" x1="0" y1="0" x2="0" y2="1">
      <stop offset="0" stop-color="#4e3a2f"/>
      <stop offset="0.45" stop-color="#6b5a3a"/>
      <stop offset="1" stop-color="#c9643a"/>
    </linearGradient>
  </defs>

  <rect class="bg-white" x="0" y="0" width="1768" height="702"/>

  <polygon class="accent-deep" points="0,0 55,0 0,112"/>
  <polygon class="accent-blue" points="62,0 92,0 0,200 0,132"/>

  <polygon role="img" aria-label="Crew member placing and finishing fresh concrete on a residential job, with a branded company shirt in the foreground" fill="url(#crewTone)" points="893,0 1735,0 1622,298 812,298"/>
  <polygon role="img" aria-label="Newly poured smooth concrete driveway in front of a brick garage" fill="url(#garageTone)" points="758,308 1255,308 1186,525 703,525"/>
  <polygon role="img" aria-label="Stamped terracotta-colored concrete walkway leading to a house" fill="url(#walkTone)" points="1256,308 1768,308 1768,635 1186,635 1186,525"/>

  <polygon class="accent-blue" points="880,0 893,0 827,168 814,168"/>
  <polygon class="accent-blue" points="1742,0 1768,0 1768,80 1705,298 1622,298"/>
  <polygon class="accent-deep" points="1768,145 1768,298 1708,298"/>

  <polygon class="bg-white" points="703,525 1525,525 1485,635 703,635"/>

  <polygon class="bg-ink" points="35,183 818,183 700,490 0,490 0,240"/>

  <polygon class="accent-blue" points="20,498 710,498 790,640 0,640 0,540"/>
  <polygon class="bg-ink" points="0,582 728,582 755,640 0,640"/>

  <rect class="bg-ink" x="0" y="644" width="1768" height="58"/>

  <rect class="accent-blue" x="148" y="36" width="88" height="88"/>
  <text class="brand-name" x="310" y="100">MARLOWE’S</text>
  <text class="brand-sub" x="312" y="128">CONSTRUCTION L.L.C</text>

  <text class="headline-main" x="52" y="306" textLength="662" lengthAdjust="spacingAndGlyphs">CONCRETE</text>
  <line class="rule" x1="66" y1="350" x2="190" y2="350"/>
  <text class="headline-mid" x="204" y="372" textLength="314" lengthAdjust="spacingAndGlyphs">BUILT FOR</text>
  <line class="rule" x1="533" y1="350" x2="692" y2="350"/>
  <text class="headline-end" x="40" y="465" textLength="624" lengthAdjust="spacingAndGlyphs">GENERATIONS</text>

  <circle cx="102" cy="539" r="29" fill="var(--ink)"/>
  <path d="M90,522 c3,-2 6,-1 7,2 l3,7 c1,2 0,4 -2,5 l-3,2 c2,5 6,9 11,11 l2,-3 c1,-2 3,-3 5,-2 l7,3 c3,1 4,4 2,7 l-3,4 c-2,2 -6,3 -9,2 c-12,-4 -21,-13 -25,-25 c-1,-3 0,-7 2,-9 z" fill="var(--brand-blue)"/>
  <text class="phone-number" x="146" y="563" textLength="505" lengthAdjust="spacingAndGlyphs">(555) 214-7630</text>

  <text class="web-address" x="100" y="625" textLength="560" lengthAdjust="spacingAndGlyphs">marlowesconstruction.example</text>

  <text class="review-name" x="793" y="608" textLength="234" lengthAdjust="spacingAndGlyphs">Zorvix</text>
  <g class="stars">
    <polygon class="star" points="1070,568 1076,581 1090,582 1079,591 1083,605 1070,597 1057,605 1061,591 1050,582 1064,581"/>
    <polygon class="star" points="1110,568 1116,581 1130,582 1119,591 1123,605 1110,597 1097,605 1101,591 1090,582 1104,581"/>
    <polygon class="star" points="1150,568 1156,581 1170,582 1159,591 1163,605 1150,597 1137,605 1141,591 1130,582 1144,581"/>
    <polygon class="star" points="1190,568 1196,581 1210,582 1199,591 1203,605 1190,597 1177,605 1181,591 1170,582 1184,581"/>
    <polygon class="star" points="1230,568 1236,581 1250,582 1239,591 1243,605 1230,597 1217,605 1221,591 1210,582 1224,581"/>
  </g>
  <line x1="1277" y1="555" x2="1277" y2="618" stroke="var(--divider)" stroke-width="2"/>

  <g class="social">
    <circle class="accent-blue" cx="1330" cy="570" r="20"/>
    <text class="social-name" x="1330" y="614" text-anchor="middle" textLength="82" lengthAdjust="spacingAndGlyphs">Chatterly</text>
    <circle class="accent-blue" cx="1426" cy="570" r="20"/>
    <text class="social-name" x="1426" y="614" text-anchor="middle" textLength="74" lengthAdjust="spacingAndGlyphs">Pixtoria</text>
  </g>

  <text x="884" y="688" text-anchor="middle">
    <tspan class="city city-white">KALAMAZOO • </tspan><tspan class="city city-blue">BATTLE CREEK</tspan><tspan class="city city-white"> • COLDWATER • </tspan><tspan class="city city-blue">GRAND RAPIDS</tspan>
  </text>
</svg>
</body>
</html>
```